Flyer-Design für Seniorenbetreuung
Zielgruppe
Wir sind eine Genossenschaft, welche ihren Immobilienbestand gern erweitern möchte. Dafür soll für unsere Partnerfirma (welche im Seniorenbetreuungssektor tätig ist) eine Flyer erdacht werden, welcher Senioren bzw. ihre Angehörigen anspricht die Wohneigentum besitzen. Viele Senioren besitzen Ein-, Mehrfamilienhäuser oder Eigentumswohnungen und können oder wollen diese nicht weiter vererben. Zusätzlich sind sie durch die Kosten des Eigentums, wie Steuern oder Instandhaltungskosten belastet. Unsere Genossenschaft bietet eine Lösung des Problems. Eine Übernahme des Eigentums bei gleichzeitigem lebenslangem Wohnrecht. Die Zielgruppe soll in dem Flyer auf die bestehende Probleme angesprochen werden und gleichzeitig eine individuelle Lösung angeboten werden, welche eine Mitgliedschaft in dem sozialen Verbund der Genossenschaft ist.
Aufgabenstellung
Der Designer hat hier völlig freie Hand. Es sollte auf die Zielgruppe passen.
Passende Texte soll sich der Designer selbst erdenken.
Nachtrag: Ich habe mittlerweile viele Zuschriften bekommen, dass die Aufgabenstellung sich Texte auszudenken etwas zu allgemein gefasst ist, daher versuche ich hier nochmal etwas Licht in Dunkle zu bringen. Ich habe genauso wenig eine Idee, wie und mit welcher Wortwahl ein Senior auf einfühlsame Weise darauf angesprochen werden soll, ob er nicht sein Haus verkaufen möchte. Meine bisherigen Ideen waren:
'Haben sie schon einmal über den Verkauf ihrer Immobilie nachgedacht? Wussten sie, dass sie ihr Wohneigentum im vollen Umfang weiter nutzen können, ohne weiter die Kosten tragen zu müssen? Sie wollen wissen wie? Rufen sie doch einfach an und ich werde ihnen genau erklären, welche Vorzüge die Mitgliedschaft in einer Genossenschaft mit sich bringt.'
Allerdings erscheint mir das viel zu direkt und ich finde nicht die richtigen Worte diese Personengruppe in dem Maße anzusprechen, wie es nötig wäre, um sie zu einem Anruf zu bewegen. Daher hatte ich gehofft, dass sie hier ein findiger Designer findet, welcher eine bessere kreative Art hat als ich.
Vielleicht ist es die falsche Plattform, vielleicht schaffen wir es nicht die Vorgaben zu spezifizieren. Bilder anzuordnen ist sicher sehr wichtig, auch ist es wichtig aufhellende Elemente einzubringen. Aber wir suchen jemanden der einen Flyer so gestalten kann das der Flyer etwas ausdrückt, das eine Botschaft vermittelt wird, das auf einem Blick der Senior den Wunsch verspürt, bei uns anzurufen. Das heißt viel wichtiger als Bilder, ist der Inhalt der Ansprache. Nicht unbedingt der Inhalt, sondern das WIE. Nochmal: wir wollen ältere Menschen dazu bewegen ihr Eigentum auf Grund von Reperaturrückstau, Überlastung, gesundheitlichen Einschränkungen, finanziellen Schwierigkeiten, zu großem Aufwand in eine Genossenschaft einzubringen. Ds heißt S..

```html
<!DOCTYPE html>
<html lang="de">
<head>
<meta charset="utf-8">
<title>Sorgenfrei im hohen Alter – Flyer</title>
<link rel="stylesheet" href="https://fonts.googleapis.com/css2?family=Fira+Sans+Condensed:wght@600&family=Fira+Sans:wght@300;400;500&family=Open+Sans:wght@600&display=swap">
<style>
  :root {
    --stage: #e8e4df;
    --paper: #fdf1d8;
    --green: #4fb48f;
    --green-dark: #3e9a79;
    --frame: #ffffff;
    --ink: #2b2b2b;
    --photo-top: #c9d4c4;
    --photo-mid: #8f9a8c;
    --photo-bottom: #4a4f4c;
  }
  * { margin: 0; padding: 0; box-sizing: border-box; }
  html, body {
    width: 1200px; height: 521px; overflow: hidden;
    background: var(--stage);
  }
  .flyer {
    position: absolute; left: 416px; top: 0;
    width: 368px; height: 521px;
    background: var(--paper);
    overflow: hidden;
  }
  .flyer__photo {
    position: absolute; left: 20px; top: 99px;
    width: 328px; height: 248px;
    background: linear-gradient(170deg, var(--photo-top) 0%, var(--photo-mid) 55%, var(--photo-bottom) 100%);
  }
  .flyer__frame {
    position: absolute; left: 44px; top: 31px;
    width: 279px; height: 459px;
    border: 3px solid var(--frame);
  }
  .flyer__title {
    position: absolute; left: 20px; top: 28px;
    font-family: "Fira Sans Condensed", sans-serif;
    font-weight: 600; font-size: 38px; line-height: 34px;
    letter-spacing: 0.6px;
    color: var(--green);
    text-transform: uppercase;
    white-space: nowrap;
  }
  .badge {
    position: absolute; left: 26px; top: 210px;
    width: 122px; height: 122px;
  }
  .badge__text {
    position: absolute; left: -10px; top: 23px; width: 142px;
    transform: rotate(-20deg);
    font-family: "Open Sans", sans-serif;
    font-weight: 600; font-size: 12.5px; line-height: 17px;
    color: #fff; text-align: center; text-transform: uppercase;
    white-space: nowrap;
  }
  .badge__stars {
    position: absolute; left: 59px; top: 91px;
    transform: rotate(-20deg);
  }
  .flyer__body {
    position: absolute; left: 56px; top: 356px; width: 197px;
    font-family: "Fira Sans", sans-serif;
    font-weight: 300; font-size: 10px; line-height: 11.5px;
    color: var(--ink);
  }
  .flyer__line {
    display: block; white-space: nowrap;
    text-align: justify; text-align-last: justify;
  }
  .flyer__line--last { text-align-last: left; }
  .contact {
    position: absolute; left: 56px; top: 456px; width: 197px;
    font-family: "Fira Sans", sans-serif;
    font-weight: 300; font-size: 10px; line-height: 12.5px;
    color: var(--ink); white-space: nowrap;
  }
  .contact__line { display: flex; align-items: center; }
  .contact__phone { color: var(--green); font-weight: 500; }
  .contact__dot {
    width: 3px; height: 3px; border-radius: 50%;
    background: var(--frame); margin-left: 14px;
  }
  .contact__hours { margin-left: auto; }
</style>
</head>
<body>
  <main class="flyer">
    <div class="flyer__photo" role="img" aria-label="Foto: älterer Mann liest Zeitung auf einem Stuhl vor einem hellen Sprossenfenster mit Blick ins Grüne"></div>
    <div class="flyer__frame"></div>
    <h1 class="flyer__title">Sorgenfrei<br>im hohen Alter</h1>

    <div class="badge">
      <svg width="122" height="122" viewBox="0 0 122 122">
        <circle cx="61" cy="61" r="60" fill="none" stroke="var(--green-dark)" stroke-width="1.5"/>
        <circle cx="61" cy="61" r="57" fill="var(--green)"/>
      </svg>
      <p class="badge__text">Mehr<br>Lebensqualität<br>im gewohnten<br>Umfeld</p>
      <svg class="badge__stars" width="34" height="10" viewBox="0 0 40 12" fill="#fff">
        <polygon points="5,0 6.3,3.8 10,3.8 7,6.1 8.1,10 5,7.6 1.9,10 3,6.1 0,3.8 3.7,3.8"/>
        <polygon points="20,0 21.3,3.8 25,3.8 22,6.1 23.1,10 20,7.6 16.9,10 18,6.1 15,3.8 18.7,3.8"/>
        <polygon points="35,0 36.3,3.8 40,3.8 37,6.1 38.1,10 35,7.6 31.9,10 33,6.1 30,3.8 33.7,3.8"/>
      </svg>
    </div>

    <p class="flyer__body">
      <span class="flyer__line">Befreien Sie sich von den hohen Kosten</span>
      <span class="flyer__line">ihrer Immobilie und lassen Sie die Steuern</span>
      <span class="flyer__line">und Instandhaltung unsere Sorge sein. Wir</span>
      <span class="flyer__line">übernehmen ihr Haus oder ihre Wohnung</span>
      <span class="flyer__line">und Sie wohnen lebenslang mietfrei in</span>
      <span class="flyer__line flyer__line--last">Ihren eigenen vier Wänden.</span>
    </p>

    <div class="contact">
      <p>Melden Sie sich kostenfrei bei uns unter:</p>
      <p class="contact__line">
        <span class="contact__phone">04321 / 9876 540</span>
        <span class="contact__dot"></span>
        <span class="contact__hours">(Mo.-Fr. 8-18 Uhr)</span>
      </p>
    </div>
  </main>
</body>
</html>
```